'Halbrook Video' - Website Template Design (that I can use in Word Press)

I would like a professional, colorful website template (4 pages) designed in a format that can be used with Word Press. Upon completion of the design, I would like to take over and maintain/host using Web Press and my Net Parrot account.

My business is videography - producing videos for companies, organizations and not-for-profit charities. Our company will do everything, including writing, planning, producing, directing filming and editing videos etc.

I have a colorful logo and business card already designed and I would like the website built around the look of the logo and business card.

I would like an index page designed first. Once the designer has created an index page I like best, I would like three more pages created with that same design.

1) A 'contact us' page
2) A page with a plug in that would allow me to upload video or connect to ClipVane to show samples of my videography
3) A general template page I could add new pages to in the future.

Target Market(s)

businesses of all kinds, organizations, governments, not-for-profit charities

Industry/Entity Type

Film Production

Number of Pages Required

4 page

Font styles to use
Sans Serif

Requirements
Must have
• 1) Index page
• 2) Contact Us page
• 2) A page with a plug in that would allow me to upload video or connect to ClipVane to show samples of my videography
• 3) A general template page I could add new pages to in the future
Nice to have
• Surprise me! I love lots of color and am open to creative ideas.

```html
<!DOCTYPE html>
<html lang="en">
<head>
<meta charset="utf-8">
<title>Halbrook Video</title>
<link href="https://fonts.googleapis.com/css2?family=Montserrat:wght@400;500;600&family=Arimo:wght@400;700&display=swap" rel="stylesheet">
<style>
:root{
  --orange:#f06522;
  --red:#e8202a;
  --yellow:#d4c01a;
  --green:#4aa829;
  --blue:#2443b3;
  --purple:#8a26b4;
  --ink:#333;
  --muted:#666;
  --card:#ebebeb;
  --footer:#161212;
  --white:#fff;
}
*{margin:0;padding:0;box-sizing:border-box}
html,body{width:686px;height:1200px;overflow:hidden;background:var(--white)}
body{font-family:Arimo,Arial,sans-serif;color:var(--ink)}
.page{position:relative;width:686px;height:1200px}
.abs{position:absolute}
h2{font-family:Montserrat,Arial,sans-serif;font-weight:500;font-size:16px;letter-spacing:.3px;display:flex;align-items:center;gap:8px}

/* header */
.header{left:0;top:0;width:686px;height:66px}
.brand{left:64px;top:14px;display:flex;align-items:center;gap:6px}
.brand-square{width:22px;height:22px;background:var(--orange)}
.brand-name{font-family:Montserrat,Arial,sans-serif;font-weight:600;font-size:10px;color:#222;line-height:1.1;width:60px}
.social{right:65px;top:15px;display:flex;gap:5px}
.social span{width:14px;height:14px;border-radius:50%;background:#ddd}
.nav{right:60px;top:42px;display:flex;gap:0;font-size:7px;text-transform:uppercase;color:#222}
.nav a{color:inherit;text-decoration:none;padding:4px 11px}
.nav a.active{background:var(--orange);color:#fff;border:1px dashed #fff;outline:2px solid var(--orange);padding:3px 9px;margin-right:2px}

/* hero */
.hero{left:0;top:66px;width:686px;height:286px;background:linear-gradient(160deg,#b7a88d 0%,#8a7b62 40%,#4e4336 80%,#2f2820 100%)}
.hero-panel{left:71px;top:143px;width:280px;height:143px;background:rgba(70,62,52,.55)}
.hero-title{left:80px;top:152px;font-family:Montserrat,Arial,sans-serif;font-size:24px;font-weight:500;color:#fff}
.hero-text{left:80px;top:187px;width:265px;font-size:6.5px;line-height:14.5px;color:#fff}
.dots{left:326px;top:267px;display:flex;gap:3px}
.dots span{width:5px;height:5px;border-radius:50%;background:#777}
.dots span.on{background:var(--orange)}

/* about */
.about{left:0;top:352px;width:686px;height:145px;background:var(--red);color:#fff}
.about h2{position:absolute;left:64px;top:30px;color:#fff}
.about-mark{left:296px;top:30px;width:88px;height:88px;background:rgba(255,255,255,.08)}
.about p{position:absolute;left:64px;top:56px;width:560px;font-size:6.4px;line-height:17.6px}
.sq{width:14px;height:14px;background:#fff;display:inline-block}

/* services */
.services{left:0;top:497px;width:686px;height:245px;background:linear-gradient(180deg,#dcdcdc,#ececec 60%,#f2f2f2)}
.services h2{position:absolute;left:64px;top:30px}
.svc{top:69px;width:129px;height:139px;color:#fff;box-shadow:0 1px 2px rgba(0,0,0,.15)}
.svc-head{position:absolute;left:13px;top:14px;display:flex;align-items:center;gap:9px;font-family:Montserrat,Arial,sans-serif;font-size:9px;font-weight:500;text-transform:uppercase}
.ring{width:30px;height:30px;border:1px solid rgba(255,255,255,.8);border-radius:50%;display:flex;align-items:center;justify-content:center}
.svc hr{position:absolute;left:10px;top:55px;width:109px;border:0;border-top:1px solid rgba(255,255,255,.35)}
.svc p{position:absolute;left:10px;top:66px;width:109px;font-size:6px;line-height:15px;text-align:justify}

/* projects */
.projects h2{position:absolute;left:64px;top:769px}
.proj{top:806px;width:176px;height:187px;background:var(--card)}
.proj-img{position:absolute;left:13px;top:12px;width:151px;height:83px}
.proj h3{position:absolute;left:13px;top:106px;font-family:Montserrat,Arial,sans-serif;font-size:7.5px;font-weight:500;color:var(--red);text-transform:uppercase}
.proj hr{position:absolute;left:13px;top:123px;width:151px;border:0;border-top:1px solid #d6d6d6}
.proj p{position:absolute;left:13px;top:133px;width:151px;font-size:6.3px;line-height:14.8px;color:var(--muted);text-align:justify}

/* newsletter */
.newsletter{left:0;top:1027px;width:686px;height:126px;background:var(--orange)}
.newsletter h2{position:absolute;left:64px;top:25px;color:#fff}
.field{top:64px;width:203px;height:31px;background:#fff;border-radius:2px;font-size:6.5px;font-style:italic;color:#999;padding:12px 11px}
.subscribe{left:497px;top:64px;width:109px;height:31px;background:var(--blue);color:#fff;border-radius:2px;font-family:Montserrat,Arial,sans-serif;font-size:8.5px;font-weight:500;text-align:center;line-height:31px}

/* footer */
.footer{left:0;top:1153px;width:686px;height:47px;background:var(--footer);color:#fff;font-size:6px}
.footer .copy{position:absolute;left:64px;top:21px}
.footer .contact{position:absolute;right:64px;top:20px;display:flex;gap:12px;align-items:center}
.footer .contact span{display:flex;gap:4px;align-items:center}
</style>
</head>
<body>
<div class="page">

  <header class="header abs">
    <div class="brand abs"><span class="brand-square"></span><span class="brand-name">HALBROOK VIDEO</span></div>
    <div class="social abs" aria-label="Social links"><span></span><span></span><span></span><span></span></div>
    <nav class="nav abs">
      <a class="active" href="#">Home</a><a href="#">About Us</a><a href="#">Services</a><a href="#">Events</a><a href="#">Projects</a><a href="#">Blog</a><a href="#">Contact Us</a>
    </nav>
  </header>

  <section class="hero abs" role="img" aria-label="Video production studio with lights, tripods and a camera">
  </section>
  <div class="hero-panel abs"></div>
  <div class="hero-title abs">VIDEO PRODUCTION</div>
  <p class="hero-text abs">Lorem ipsum dolor sit amet, consectetur adipiscing elit. Ut magna velit, congue vel placerat id, egestas a odio. Nam et tristique nisl. Phasellus quis erat neque.</p>
  <div class="dots abs"><span></span><span></span><span class="on"></span><span></span></div>

  <section class="about abs">
    <div class="about-mark abs"></div>
    <h2><span class="sq"></span>ABOUT HALBROOK VIDEO</h2>
    <p>Lorem ipsum dolor sit amet, consectetur adipiscing elit. Ut magna velit, congue vel placerat id, egestas a odio. Nam et tristique nisl. Phasellus quis erat neque. Vivamus et nisi id erat posuere ultrices quis vel ligula. Nam pellentesque cursus quam. Mauris mi magna, auctor vel leo vel, ullamcorper suscipit arcu. Quisque eget odio ut libero lacinia blandit. Donec consequat aliquet nulla, id egestas orci pellentesque id. Pellentesque quis laoreet ligula. Vestibulum sapien velit, lobortis vitae vulputate ac, viverra sed magna. Vivamus ut odio turpis.</p>
  </section>

  <section class="services abs" role="img" aria-label="Faded camera operator background">
    <h2><svg width="15" height="15" viewBox="0 0 16 16"><circle cx="8" cy="8" r="5" fill="none" stroke="#f06522" stroke-width="3" stroke-dasharray="2.2 1.4"/><circle cx="8" cy="8" r="4.2" fill="none" stroke="#f06522" stroke-width="1.6"/><circle cx="8" cy="8" r="1.5" fill="#f06522"/></svg>SERVICES</h2>

    <div class="svc abs" style="left:64px;background:var(--yellow)">
      <div class="svc-head"><span class="ring"><svg width="14" height="14" viewBox="0 0 14 14"><path d="M3 11l1-3 6-6 2 2-6 6z" fill="none" stroke="#fff"/></svg></span>Writing</div>
      <hr><p>Vivamus et nisi id erat posuere ult ric es quis vel ligula. Nam pellentesque cur sus quam. Mauris mi magna, auctor vel leo vel, ullamcorper.</p>
    </div>
    <div class="svc abs" style="left:207px;background:var(--green)">
      <div class="svc-head"><span class="ring"><svg width="14" height="14" viewBox="0 0 14 14"><rect x="3" y="2" width="9" height="10" fill="none" stroke="#fff"/><path d="M5 5h5M5 7.5h5M5 10h5" stroke="#fff"/></svg></span>Planning</div>
      <hr><p>Cras lacus magna, fringilla venenatis nibh quis, congue fringilla arcu. Interdum et malesuada fames ac ante ipsum primis in faucibus.</p>
    </div>
    <div class="svc abs" style="left:350px;background:var(--blue)">
      <div class="svc-head"><span class="ring"><svg width="16" height="14" viewBox="0 0 16 14"><circle cx="5" cy="7" r="3" fill="none" stroke="#fff"/><circle cx="11" cy="7" r="3" fill="none" stroke="#fff"/><rect x="2" y="3" width="12" height="8" rx="1" fill="none" stroke="#fff"/></svg></span>Producing</div>
      <hr><p>Mauris dui tortor, blandit nec diam congue, sagittis feugiat massa. Suspendisse eget porttitor nibh, vulputate interdum mauris.</p>
    </div>
    <div class="svc abs" style="left:493px;background:var(--purple)">
      <div class="svc-head"><span class="ring"><svg width="14" height="14" viewBox="0 0 14 14"><rect x="2" y="2" width="10" height="10" fill="none" stroke="#fff"/><path d="M4 2v10M10 2v10" stroke="#fff"/><path d="M6 5l2.5 2L6 9z" fill="#fff"/></svg></span>Filming</div>
      <hr><p>Vivamus et nisi id erat posuere ult ric es quis vel ligula. Nam pellentesque cur sus quam. Mauris mi magna, auctor vel leo vel, ullamcorper.</p>
    </div>
  </section>

  <section class="projects">
    <h2><svg width="15" height="15" viewBox="0 0 16 16"><circle cx="8" cy="8" r="6.5" fill="none" stroke="#f06522" stroke-width="1.5"/><path d="M6.5 5l4 3-4 3z" fill="#f06522"/></svg>RECENT PROJECTS</h2>

    <article class="proj abs" style="left:64px">
      <div class="proj-img" role="img" aria-label="Camera crew filming outdoors" style="background:linear-gradient(160deg,#6d5a48,#3a3530 60%,#8c8c88)"></div>
      <h3>Lorem ipsum dolor sit amet</h3><hr>
      <p>Quisque eget odio ut libero lacinia blandit. Donec consequat aliquet nulla, id egestas orci pellente sque id. Pellentesque quis laoreet ligula.</p>
    </article>
    <article class="proj abs" style="left:255px">
      <div class="proj-img" role="img" aria-label="Actor holding a clapperboard, video play button" style="background:linear-gradient(160deg,#c9a27a,#7a5a44 55%,#3e3430)">
        <svg class="abs" style="left:63px;top:29px" width="25" height="25" viewBox="0 0 26 26"><circle cx="13" cy="13" r="11.5" fill="rgba(255,255,255,.15)" stroke="#fff" stroke-width="1.5"/><path d="M10.5 8l7 5-7 5z" fill="#fff"/></svg>
      </div>
      <h3>Praesent sodales vel tellus</h3><hr>
      <p>Quisque eget odio ut libero lacinia blandit. Donec consequat aliquet nulla, id egestas orci pellente sque id. Pellentesque quis laoreet ligula.</p>
    </article>
    <article class="proj abs" style="left:446px">
      <div class="proj-img" role="img" aria-label="Camera operator reviewing footage" style="background:linear-gradient(160deg,#a0744e,#4a3426 55%,#1e1a18)"></div>
      <h3>Class aptent taciti sociosqu</h3><hr>
      <p>Quisque eget odio ut libero lacinia blandit. Donec consequat aliquet nulla, id egestas orci pellente sque id. Pellentesque quis laoreet ligula.</p>
    </article>
  </section>

  <section class="newsletter abs">
    <h2><svg width="17" height="13" viewBox="0 0 17 13"><rect x=".75" y=".75" width="15.5" height="11.5" fill="none" stroke="#fff" stroke-width="1.3"/><path d="M1 1l7.5 6L16 1M1 12l5.5-5M16 12l-5.5-5" fill="none" stroke="#fff" stroke-width="1.1"/></svg>SIGNUP OUR NEWSLETTER</h2>
    <div class="field abs" style="left:64px">Name</div>
    <div class="field abs" style="left:280px">Email Address</div>
    <div class="subscribe abs">SUBSCRIBE</div>
  </section>

  <footer class="footer abs">
    <div class="copy">Copyright@2016 Halbrook Video. All Right Reserved.</div>
    <div class="contact">
      <span><svg width="7" height="7" viewBox="0 0 10 10"><path d="M2 1l2 2-1 1.5c.8 1.3 1.5 2 2.5 2.5L7 6l2 2-1.5 1.5C4.5 9 1 5.5.5 2.5z" fill="#f06522"/></svg>03 555 01987</span>
      <span><svg width="8" height="6" viewBox="0 0 10 7"><rect width="10" height="7" fill="#f06522"/><path d="M0 0l5 4 5-4" fill="none" stroke="#161212" stroke-width=".8"/></svg>hello@halbrookvideo.net</span>
    </div>
  </footer>

</div>
</body>
</html>
```